Amber Thread Initiative at The Harbor Lantern

I am looking for a poster that I can hang (long term) in a hospital or other clinic (cancer clinic, physiotherapy clinic). The poster should convey that Pilates is the best way to get back into movement after surgery/radiation/chemotherapy. Pilates will keep you moving efficiently, prevent imbalances, improve blood flow to name a few. My website is theharborlantern.example for details of my studio and the website to look at for further details on the program and full list of benefits is amberthreadinitiative.example.

Target Market(s)

Breast cancer survivors

Industry/Entity Type

Clinic

Requirements
Must have
• Must convey my program training/certification, my high quality of teaching, clients are in a safe, supportive place.
• My studio address, my name.
Nice to have
• We offer this work in both a group setting or privately (one to one).

```html
<!DOCTYPE html>
<html lang="en">
<head>
<meta charset="utf-8">
<title>Amber Thread Initiative — The Harbor Lantern</title>
<link rel="stylesheet" href="https://fonts.googleapis.com/css2?family=Arimo:wght@700&family=Montserrat:wght@300;400;600;700&display=swap">
<style>
  :root {
    --backdrop: #e8e2e2;
    --paper: #ffffff;
    --rose: #c0647a;
    --rose-band: #f08399;
    --rose-deep: #c96a80;
    --rose-panel: rgba(196, 104, 128, 0.88);
    --strip: #f08399;
    --charcoal: #3f3f41;
    --ink: #3a3a3a;
    --white: #ffffff;
  }
  * { box-sizing: border-box; margin: 0; padding: 0; }
  html, body { width: 1200px; height: 1200px; overflow: hidden; background: var(--backdrop); }
  .poster {
    position: absolute; left: 208px; top: 0; width: 784px; height: 1200px;
    background: var(--paper); overflow: hidden;
    font-family: "Montserrat", sans-serif;
  }
  .headline {
    position: absolute; left: 45px; top: 34px; width: 720px;
    font-family: "Arimo", sans-serif; font-weight: 700;
    font-size: 57px; line-height: 58px; letter-spacing: 1.2px;
    color: var(--rose); text-transform: uppercase; white-space: nowrap;
  }
  .intro {
    position: absolute; left: 45px; top: 166px; width: 697px;
    column-count: 2; column-gap: 23px;
    font-weight: 300; font-size: 13.4px; line-height: 16.4px;
    color: var(--ink); text-align: justify;
  }
  .hero-photo {
    position: absolute; left: 0; top: 325px; width: 784px; height: 455px;
    background:
      linear-gradient(180deg, rgba(255,255,255,0) 70%, rgba(40,40,48,0.55) 92%, rgba(30,30,36,0.8) 100%),
      linear-gradient(100deg, #f6f5f3 0%, #eeece9 28%, #d9cfc5 36%, #3b3d47 46%, #2d303b 53%, #5766b4 61%, #3b4aa0 65%, #2c2e38 72%, #2a2b33 77%, #cf4a78 84%, #e47a9c 88%, #eeebe8 95%, #f7f7f5 100%);
  }
  .wave { position: absolute; left: 0; top: 300px; width: 784px; height: 120px; }
  .benefits {
    position: absolute; left: 46px; top: 423px; width: 173px; height: 323px;
    background: var(--rose-panel); border-radius: 5px;
    padding: 12px 12px 0 12px; color: var(--white);
  }
  .benefits h2 { font-weight: 700; font-size: 14px; line-height: 16px; margin-bottom: 15px; }
  .benefits ul { list-style: none; }
  .benefits li {
    position: relative; padding-left: 18px;
    font-weight: 400; font-size: 11px; line-height: 13.8px;
  }
  .benefits li::before {
    content: ""; position: absolute; left: 2px; top: 5px;
    width: 4px; height: 4px; border-radius: 50%; background: var(--white);
  }
  .strip { position: absolute; left: 0; top: 780px; width: 784px; height: 162px; background: var(--strip); }
  .strip-photo { position: absolute; top: 14px; height: 134px; }
  .strip-photo.left {
    left: 0; width: 186px;
    background:
      linear-gradient(180deg, rgba(255,255,255,0) 78%, #f3c6d3 100%),
      linear-gradient(90deg, #ffffff 0%, #f6d0dc 20%, #2f2a2c 38%, #f2a9c0 52%, #e57ba0 66%, #d86790 80%, #fbeff3 92%, #ffffff 100%);
  }
  .strip-photo.right {
    left: 615px; width: 169px;
    background:
      linear-gradient(180deg, rgba(255,255,255,0) 78%, #f3c6d3 100%),
      linear-gradient(90deg, #ffffff 0%, #fdf5f7 30%, #f2a0bb 45%, #ef8fae 55%, #2f2a2c 62%, #fdf5f7 75%, #ffffff 100%);
  }
  .program-mark {
    position: absolute; left: 202px; top: 14px; width: 396px; height: 134px;
    background: var(--white); display: flex; align-items: center; justify-content: center; gap: 12px;
  }
  .program-mark .dot { width: 18px; height: 18px; border-radius: 50%; background: var(--rose-band); }
  .program-mark .name { font-weight: 400; font-size: 24px; color: #3a3a3a; letter-spacing: 0.5px; }
  .footer { position: absolute; left: 0; top: 942px; width: 784px; height: 258px; background: var(--charcoal); color: var(--white); }
  .portrait {
    position: absolute; left: 31px; top: 43px; width: 152px; height: 152px; border-radius: 50%;
    background: linear-gradient(180deg, #dcd7d2 0%, #c9bdb3 35%, #6b4a3c 55%, #4a4fb0 80%, #3d44a6 100%);
    border: 2px solid #6b6b6d;
  }
  .instructor { position: absolute; left: 0; top: 206px; width: 214px; text-align: center; font-weight: 700; font-size: 9px; letter-spacing: 0.2px; }
  .credentials { position: absolute; left: 211px; top: 64px; width: 440px; list-style: none; }
  .credentials li {
    position: relative; padding-left: 20px; margin-bottom: 6px;
    font-weight: 700; font-size: 16px; line-height: 19px; text-transform: uppercase;
  }
  .credentials svg { position: absolute; left: 0; top: 5px; width: 12px; height: 12px; }
  .studio-mark { position: absolute; left: 655px; top: 70px; width: 115px; text-align: center; }
  .studio-mark .name { font-weight: 300; font-size: 18px; line-height: 26px; letter-spacing: 2px; text-transform: uppercase; color: var(--white); }
  .studio-mark .dot { display: block; margin: 0 auto 12px; width: 40px; height: 40px; border-radius: 50%; background: var(--white); }
  .contact { position: absolute; left: 120px; top: 228px; width: 650px; text-align: center; font-size: 8.6px; font-weight: 400; }
</style>
</head>
<body>
<main class="poster">
  <h1 class="headline">Get back to living…<br>not just surviving</h1>

  <p class="intro">The life-force of the Amber Thread Initiative is to ensure that every woman has the ability to regain a sense of wellbeing that had been lost from diagnosis through surgery and into recovery. This can be achieved, in part, through an exercise therapy program designed specifically for the needs and challenges facing the growing number of breast cancer survivors. Rehabilitation is a key component often missing in the treatment of breast cancer. The Amber Thread Initiative has been created to enhance recovery for breast cancer patients. The program helps stretch and strengthens shoulder, chest, and back allowing the patient to improve range of motion and strength to those areas most affected by breast cancer surgery, treatment and reconstruction.</p>

  <div class="hero-photo" role="img" aria-label="Photo of four women in dark, blue and pink workout tops exercising side by side on Pilates tower equipment in a bright white studio, arms reaching forward"></div>

  <svg class="wave" viewBox="0 300 784 120" preserveAspectRatio="none" aria-hidden="true">
    <path d="M0,300 H784 V322 C720,368 640,392 560,384 C460,372 380,330 280,322 C180,314 80,330 0,352 Z" fill="var(--paper)"/>
    <path d="M0,352 C80,330 180,314 280,322 C380,330 460,372 560,384 C640,392 720,368 784,322 V340 C720,388 640,404 560,398 C460,390 380,352 280,346 C170,340 80,376 0,412 Z" fill="var(--rose-band)"/>
    <path d="M0,412 C80,376 170,340 280,346 C380,352 460,390 560,398 C640,404 720,388 784,340 V346 C720,394 640,410 560,404 C460,398 380,366 280,364 C170,362 80,394 0,420 Z" fill="var(--rose-deep)"/>
  </svg>

  <section class="benefits">
    <h2>Benefits of the Amber Thread Initiative</h2>
    <ul>
      <li>Regain Strength and Mobility in Affected Shoulder &amp; Arm</li>
      <li>Promotes Lymphatic Drainage, Helping to Prevent Lymphedema</li>
      <li>Improves Functional Ability &amp; Quality of Life</li>
      <li>Enhances &amp; Restores Energy Levels</li>
      <li>Assists in Restoring Posture</li>
      <li>Decreases Stress &amp; Anxiety</li>
      <li>Alleviates Pain &amp; Swelling</li>
    </ul>
  </section>

  <section class="strip">
    <div class="strip-photo left" role="img" aria-label="Photo of a woman in a pink top in child's pose stretching over a pink exercise ball"></div>
    <div class="program-mark"><span class="dot"></span><span class="name">Amber Thread Initiative</span></div>
    <div class="strip-photo right" role="img" aria-label="Photo of a woman in a pink top seated on a mat reaching one arm overhead"></div>
  </section>

  <footer class="footer">
    <div class="portrait" role="img" aria-label="Portrait photo of the instructor in a blue top"></div>
    <p class="instructor">MAREN HOLLOWAY</p>
    <ul class="credentials">
      <li><svg viewBox="0 0 12 12"><path d="M1,7 L4.5,10.5 L11,1.5" fill="none" stroke="#fff" stroke-width="1.2"/></svg>15 years of teaching</li>
      <li><svg viewBox="0 0 12 12"><path d="M1,7 L4.5,10.5 L11,1.5" fill="none" stroke="#fff" stroke-width="1.2"/></svg>Successful results with previous breast cancer survivors</li>
      <li><svg viewBox="0 0 12 12"><path d="M1,7 L4.5,10.5 L11,1.5" fill="none" stroke="#fff" stroke-width="1.2"/></svg>A passion to get people out of their pain</li>
    </ul>
    <div class="studio-mark"><span class="dot"></span><span class="name">The Harbor Lantern</span></div>
    <p class="contact">Contact: #204-118 Larkspur Ave., Brookhaven, B.C., Canada, V0X 1A0, 555.010.2639, info@theharborlantern.example</p>
  </footer>
</main>
</body>
</html>
```